Business Card Design

We sell fish products to corporate food companies who then turn these products into final food products for consumers

Industry/Entity Type

Business

Contact Information for Business Card

I need a corporate business card template for a fish products business. We would like it be professional for use in dealing with multi national companies. This company business card template will be used by multiple employees so the following fields must be open to edit (Name, Phone Number and Email address)

```html
<!DOCTYPE html>
<html lang="en">
<head>
<meta charset="utf-8">
<title>Tidewell Seafoods – Business Card</title>
<link rel="stylesheet" href="https://fonts.googleapis.com/css2?family=Marcellus&family=Oswald:wght@600&family=Montserrat:wght@500&display=swap">
<style>
  :root {
    --sea-deep: #4f93cf;
    --sea-mid: #7fbbe6;
    --sea-light: #bfe4f7;
    --sea-haze: #d9f0fb;
    --brand-blue: #0d4f9e;
    --name-blue: #0b58b0;
    --rule-green: #6fc08a;
    --rule-blue: #3f88c8;
    --ink-navy: #0f2d57;
    --address-blue: #4a6fa8;
  }
  * { margin: 0; padding: 0; box-sizing: border-box; }
  html, body {
    width: 1200px;
    height: 702px;
    overflow: hidden;
    background: #ffffff;
  }
  .card {
    position: relative;
    width: 1200px;
    height: 702px;
    overflow: hidden;
  }
  .sea-backdrop {
    position: absolute;
    inset: 0;
    background:
      radial-gradient(ellipse 60% 45% at 70% 22%, var(--sea-haze) 0%, transparent 70%),
      radial-gradient(ellipse 70% 50% at 20% 85%, var(--sea-deep) 0%, transparent 75%),
      linear-gradient(180deg, var(--sea-light) 0%, var(--sea-mid) 55%, var(--sea-deep) 100%);
  }
  .brand {
    position: absolute;
    left: 61px;
    top: 52px;
    width: 560px;
    text-align: center;
    font-family: "Marcellus", serif;
    color: var(--brand-blue);
  }
  .brand-dot {
    display: block;
    width: 120px;
    height: 120px;
    margin: 0 auto 26px;
    border-radius: 50%;
    background: var(--brand-blue);
  }
  .brand-name {
    font-size: 86px;
    line-height: 1;
    letter-spacing: 1px;
  }
  .brand-sub {
    display: block;
    margin-top: 14px;
    font-size: 44px;
    letter-spacing: 14px;
    line-height: 1;
  }
  .contact {
    position: absolute;
    right: 58px;
    top: 346px;
    width: 655px;
    text-align: right;
  }
  .contact-name {
    font-family: "Oswald", sans-serif;
    font-weight: 600;
    font-style: italic;
    font-size: 90px;
    line-height: 1;
    color: var(--name-blue);
    text-shadow: 2px 3px 0 #ffffff, 4px 6px 8px rgba(15, 45, 87, 0.35);
    transform: scaleX(0.9);
    transform-origin: right center;
    letter-spacing: -1px;
  }
  .contact-rule {
    width: 652px;
    height: 4px;
    margin: 6px 0 8px auto;
    background: linear-gradient(90deg, var(--rule-blue), var(--rule-green));
  }
  .contact-phone,
  .contact-email {
    font-family: "Montserrat", sans-serif;
    font-weight: 500;
    color: var(--ink-navy);
    line-height: 1.12;
  }
  .contact-phone { font-size: 35px; letter-spacing: 2px; }
  .contact-email { font-size: 42px; letter-spacing: 1px; }
  .address {
    position: absolute;
    left: 0;
    right: 0;
    top: 592px;
    text-align: center;
    font-family: "Montserrat", sans-serif;
    font-weight: 500;
    font-size: 32px;
    letter-spacing: 2px;
    color: var(--address-blue);
    opacity: 0.8;
    text-shadow: 0 0 6px rgba(255, 255, 255, 0.7);
  }
</style>
</head>
<body>
  <main class="card">
    <div class="sea-backdrop" role="img" aria-label="Textured ocean water surface in light and mid blues"></div>

    <header class="brand">
      <span class="brand-dot"></span>
      <div class="brand-name">TIDEWELL</div>
      <span class="brand-sub">SEAFOODS</span>
    </header>

    <section class="contact">
      <div class="contact-name">DANIEL REYES</div>
      <div class="contact-rule"></div>
      <div class="contact-phone">+34 911 48 20 57</div>
      <div class="contact-email">d.reyes@tidewell.com</div>
    </section>

    <footer class="address">48 Harbor Point Road, Millbrook, NJ 07102</footer>
  </main>
</body>
</html>
```